Book cover for publishing doctoral research about various national styles of piano playing.

I need a book cover for a publication of a doctoral research with regard to styles of piano performance characteristic to various nations.

Any images or graphics are optional, typography seems most important, but please feel free to be creative.

I attach the barcode, qsr and publisher's logo in the next few days. (Logo is still being designed).

For various reasons the size of the book is not completely decided yet. Please create your design in 7" x 10", but if at all possible, I would like to ask for files of two sizes, also including 8.5" x 11" in the final submission.

I am looking for a design that looks professional, probably simple, but I am open to any suggestions.

Dear Designers,I would like to thank you all for participation and submitting so many high-quality designs.My final decision was based on the feedback I received from my professional colleagues and potential readers.I would like to wish you all the best for the future.Best wishes,Tadeusz Added Monday, December 21, 2015

Pianists, students, music professionals

Publishing

• Title: Unfolding Seven Harbour Lullabies
• Subtitle: Memories and departures
• Author: Tadeusz Jarocki
• Space for my logo on the front page and the spine.
• On the back page, please include some space for a short biography, 'barcode' and 'qsr' code.
• Please include whatever else you consider necessary.
• Would it be possible to use the same cover to a e-book edition?

```html
<!DOCTYPE html>
<html lang="en">
<head>
<meta charset="utf-8">
<title>Unfolding Seven Harbour Lullabies — Cover Set</title>
<link rel="stylesheet" href="https://fonts.googleapis.com/css2?family=Josefin+Sans:wght@300;400;700&family=PT+Sans&display=swap">
<style>
  :root {
    --yellow: #FDE674;
    --black: #231F20;
    --white: #FFFFFF;
  }
  html, body {
    margin: 0;
    padding: 0;
    width: 1200px;
    height: 1200px;
    overflow: hidden;
    background: var(--white);
  }
  .cover-sheet { display: block; width: 1200px; height: 1200px; }

  .theme-yellow { --paper: var(--yellow); --ink: var(--black); --box: var(--black); --boxink: var(--white); }
  .theme-white  { --paper: var(--white);  --ink: var(--black); --box: var(--black); --boxink: var(--white); }
  .theme-black  { --paper: var(--black);  --ink: var(--white); --box: var(--black); --boxink: var(--white); }
  .theme-bare   { --paper: transparent;   --ink: var(--black); --box: var(--black); --boxink: var(--white); }

  .paper { fill: var(--paper); }
  .rule { stroke: var(--ink); stroke-width: 3.5; fill: none; }
  .placeholder-box { fill: var(--box); }
  .placeholder-label {
    fill: var(--boxink);
    font-family: "PT Sans", sans-serif;
    font-size: 7px;
    text-anchor: middle;
  }
  .title-line {
    fill: var(--ink);
    font-family: "Josefin Sans", sans-serif;
    font-weight: 300;
  }
  .subtitle-line {
    fill: var(--ink);
    font-family: "Josefin Sans", sans-serif;
    font-weight: 700;
    font-size: 11px;
    letter-spacing: -0.6px;
  }
  .author-line {
    fill: var(--ink);
    font-family: "Josefin Sans", sans-serif;
    font-weight: 400;
  }
  .back-author {
    fill: var(--ink);
    font-family: "Josefin Sans", sans-serif;
    font-weight: 400;
    font-size: 21px;
    letter-spacing: -0.8px;
    text-anchor: middle;
  }
  .bio-placeholder {
    fill: var(--ink);
    font-family: "PT Sans", sans-serif;
    font-size: 28px;
    text-anchor: middle;
  }
  .spine-title {
    fill: var(--ink);
    font-family: "Josefin Sans", sans-serif;
    font-weight: 300;
    font-size: 20px;
  }
  .spine-author {
    fill: var(--ink);
    font-family: "Josefin Sans", sans-serif;
    font-weight: 700;
    font-size: 11px;
  }
</style>
</head>
<body>
<svg class="cover-sheet" viewBox="0 0 1500 1500" xmlns="http://www.w3.org/2000/svg">
  <defs>
    <!-- Front cover -->
    <symbol id="front-cover" viewBox="0 0 410 593" width="410" height="593" overflow="visible">
      <rect class="paper" width="410" height="593"/>
      <rect class="placeholder-box" x="22" y="25" width="63" height="64"/>
      <text class="placeholder-label" x="53.5" y="59.5">LOGO</text>
      <rect class="placeholder-box" x="108" y="25" width="63" height="64"/>
      <text class="placeholder-label" x="139.5" y="47">PUBLISHER</text>
      <text class="placeholder-label" x="139.5" y="67">LOGO</text>

      <path class="rule" d="M360 0 V185 M319 180 V593 M0 183 H178 M320 306 H410 M0 361 H140"/>

      <text class="title-line" x="155" y="226" font-size="64" textLength="250" lengthAdjust="spacingAndGlyphs">UNFOLDING</text>
      <text class="title-line" x="170" y="311" font-size="64" textLength="150" lengthAdjust="spacingAndGlyphs">SEVEN</text>
      <text class="title-line" x="60" y="379" font-size="64" textLength="210" lengthAdjust="spacingAndGlyphs">HARBOUR</text>
      <text class="title-line" x="80" y="444" font-size="58" textLength="220" lengthAdjust="spacingAndGlyphs">LULLABIES</text>

      <text class="subtitle-line" x="336" y="414">MEMORIES</text>
      <text class="subtitle-line" x="336" y="427">AND</text>
      <text class="subtitle-line" x="336" y="441">DEPARTURES</text>

      <text class="author-line" x="140" y="523" font-size="46" textLength="160" lengthAdjust="spacingAndGlyphs">TADEUSZ</text>
      <text class="author-line" x="150" y="559" font-size="46" textLength="150" lengthAdjust="spacingAndGlyphs">JAROCKI</text>
    </symbol>

    <!-- Back cover -->
    <symbol id="back-cover" viewBox="0 0 410 592" width="410" height="592" overflow="visible">
      <rect class="paper" width="410" height="592"/>
      <text class="back-author" x="205" y="151">TADEUSZ</text>
      <text class="back-author" x="205" y="170">JAROCKI</text>
      <path class="rule" d="M0 182 H410 M0 361 H410"/>
      <text class="bio-placeholder" x="205" y="282">(description biography)</text>
      <rect class="placeholder-box" x="30" y="499" width="64" height="64"/>
      <text class="placeholder-label" x="62" y="533.5">BARCODE</text>
      <rect class="placeholder-box" x="322" y="501" width="64" height="64"/>
      <text class="placeholder-label" x="354" y="523">QSR</text>
      <text class="placeholder-label" x="354" y="543">CODE</text>
    </symbol>

    <!-- Spine with logos at the head -->
    <symbol id="spine" viewBox="0 0 69 588" width="69" height="588" overflow="visible">
      <rect class="paper" width="69" height="588"/>
      <rect class="placeholder-box" x="7" y="22" width="56" height="56"/>
      <text class="placeholder-label" transform="translate(37.5 50) rotate(90)">LOGO</text>
      <rect class="placeholder-box" x="7" y="98" width="56" height="56"/>
      <text class="placeholder-label" transform="translate(43 126) rotate(90)">PUBLISHER</text>
      <text class="placeholder-label" transform="translate(31 126) rotate(90)">LOGO</text>
      <path class="rule" d="M0 180 H69 M0 358 H69"/>
      <text class="spine-title" transform="translate(44 192) rotate(90)" textLength="152" lengthAdjust="spacingAndGlyphs">UNFOLDING SEVEN</text>
      <text class="spine-title" transform="translate(22 192) rotate(90)" textLength="152" lengthAdjust="spacingAndGlyphs">HARBOUR LULLABIES</text>
      <text class="spine-author" transform="translate(29 412) rotate(90)" textLength="122" lengthAdjust="spacingAndGlyphs">TADEUSZ JAROCKI</text>
    </symbol>
  </defs>

  <!-- Front covers -->
  <use href="#front-cover" class="theme-yellow" x="23" y="157"/>
  <use href="#front-cover" class="theme-white" x="456" y="157"/>
  <use href="#front-cover" class="theme-black" x="889" y="157"/>

  <!-- Spines -->
  <use href="#spine" class="theme-yellow" x="1324" y="160"/>
  <use href="#spine" class="theme-bare" x="1418" y="160"/>

  <!-- Back covers -->
  <use href="#back-cover" class="theme-yellow" x="23" y="773"/>
  <use href="#back-cover" class="theme-white" x="456" y="773"/>
  <use href="#back-cover" class="theme-black" x="889" y="773"/>

  <!-- Black full-length spine -->
  <g class="theme-black" transform="translate(1371 777)">
    <rect class="paper" width="69" height="584"/>
    <text class="placeholder-label" transform="translate(37.5 48) rotate(90)">LOGO</text>
    <text class="placeholder-label" transform="translate(43 123) rotate(90)">PUBLISHER</text>
    <text class="placeholder-label" transform="translate(31 123) rotate(90)">LOGO</text>
    <path class="rule" d="M0 178 H69 M0 358 H69"/>
    <text class="spine-title" transform="translate(46 192) rotate(90)" textLength="152" lengthAdjust="spacingAndGlyphs">UNFOLDING SEVEN</text>
    <text class="spine-title" transform="translate(24 192) rotate(90)" textLength="152" lengthAdjust="spacingAndGlyphs">HARBOUR LULLABIES</text>
    <text class="spine-author" transform="translate(29 408) rotate(90)" textLength="122" lengthAdjust="spacingAndGlyphs">TADEUSZ JAROCKI</text>
  </g>
</svg>
</body>
</html>
```